Brisk Lending Benefits Summary

We are looking to put our benefits information into a summary document and make it look pretty/easy to read! I put all of the information together into a document, one tab for all of our medical plans and another for dental/vision. This document is only there as a guide. I want this to be visually appealing, so feel free to get creative with the format.

Industry/Entity Type

Mortgage Lender

Colors
31b7a3
ffcf3e

Requirements
Should not have
• I don't want a copy and pasted version of the visual I sent, with our logo attached.

```html
<!DOCTYPE html>
<html lang="en">
<head>
<meta charset="utf-8">
<title>Brisk Lending Benefits Summary</title>
<link rel="stylesheet" href="https://fonts.googleapis.com/css2?family=Montserrat:wght@400;600;700&family=Playfair+Display:wght@400&display=swap">
<style>
:root{
  --bg:#eef0f3;
  --paper:#ffffff;
  --ink:#2a2f45;
  --muted:#6b7080;
  --teal:#31b7a3;
  --yellow:#f8e032;
  --yellow-soft:#fbf2a6;
  --orange:#f6b24a;
  --orange-soft:#fbd9a4;
  --sky:#6fbfe6;
  --sky-soft:#c6e4f4;
  --lilac:#9c9ee0;
  --lilac-soft:#d2d2f1;
  --navy:#1f1c4d;
  --plum-soft:#a59ccb;
  --label:#e3e4ea;
  --band:#d4d5dc;
  --coral:#e8755c;
  --coral-soft:#f8cbbf;
  --dental-row:#dcdcef;
}
*{box-sizing:border-box;margin:0;padding:0}
html,body{width:720px;height:1200px;overflow:hidden;background:var(--bg)}
body{font-family:"Montserrat",Arial,sans-serif;color:var(--ink);position:relative}
.page{position:absolute;left:20px;width:680px;background:var(--paper);box-shadow:0 2px 8px rgba(0,0,0,.12);padding:18px 24px}
.page--medical{top:40px;height:540px}
.page--dental{top:620px;height:540px}
.page-head{display:flex;justify-content:space-between;align-items:flex-start;height:48px}
.brand{color:var(--teal);font-weight:700;font-size:17px;letter-spacing:-.2px;line-height:1}
.page-title{font-family:"Playfair Display",Georgia,serif;font-size:22px;font-weight:400;color:var(--navy);margin-top:4px}

/* medical grid */
.plan-grid{display:grid;grid-template-columns:150px repeat(10,1fr);font-size:5.6px;line-height:1.2}
.plan-grid > div{padding:2px 3px;height:19px;display:flex;align-items:center}
.plan-head{height:44px !important;grid-column:span 2;flex-direction:column;align-items:flex-start !important;justify-content:center;font-size:6.4px;font-weight:600}
.plan-head small{font-weight:400;font-size:5.4px;margin-top:2px}
.corner{height:44px !important;background:var(--label)}
.row-label{background:var(--label);font-weight:600;color:#444a5c}
.c1{background:var(--yellow-soft)}.h1{background:var(--yellow)}
.c2{background:var(--orange-soft)}.h2{background:var(--orange)}
.c3{background:var(--sky-soft)}.h3{background:var(--sky);color:#fff}
.c4{background:var(--lilac-soft)}.h4{background:var(--lilac);color:#fff}
.c5{background:var(--plum-soft);color:#fff}.h5{background:var(--navy);color:#fff}
.plan-grid .sub{height:13px;font-weight:600;font-size:5px}
.cost-band{display:grid;grid-template-columns:150px repeat(5,1fr);background:var(--band);margin-top:4px;font-size:5.6px}
.cost-band > div{padding:5px 3px;line-height:1.55}
.cost-band .cost-label{font-weight:600}
.cost-band .cost-value{font-weight:700;text-align:center}
.badges{display:grid;grid-template-columns:150px repeat(5,1fr);margin-top:10px;align-items:center}
.badge-note{font-size:5.6px;color:var(--muted);line-height:1.5}
.badge{width:60px;height:60px;border-radius:50%;margin:0 auto;display:flex;flex-direction:column;align-items:center;justify-content:center;font-size:6px;font-weight:700;text-align:center;line-height:1.3}
.badge span{font-size:9px}
.b1{background:var(--yellow)}.b2{background:var(--orange)}.b3{background:var(--sky);color:#fff}.b4{background:var(--lilac);color:#fff}.b5{background:var(--navy);color:#fff}
.footnote{position:absolute;left:24px;right:24px;bottom:16px;font-size:4.6px;color:var(--muted);line-height:1.5}

/* vision / dental */
.vd-layout{position:relative;height:420px}
.vision{position:absolute;left:0;top:0;width:240px}
.vision-head{background:var(--coral);color:#fff;font-weight:700;font-size:8px;padding:6px 6px;height:30px;display:flex;align-items:center}
.vd-table{width:100%;border-collapse:collapse;font-size:5.4px;line-height:1.25}
.vd-table td,.vd-table th{padding:3px 4px;vertical-align:top;text-align:left}
.vision .vd-table .lbl{background:var(--label);font-weight:600;width:46%}
.vision .vd-table .val{background:var(--coral-soft)}
.vision .vd-table tr:nth-child(even) .val{background:#f3b8a8}
.vision-badge{position:absolute;left:120px;top:340px;width:56px;height:56px;border-radius:50%;background:var(--coral);color:#fff;font-size:6px;font-weight:700;display:flex;flex-direction:column;align-items:center;justify-content:center;text-align:center;line-height:1.3}
.vision-badge span,.dental-badge span{font-size:9px}
.vision-note{position:absolute;left:0;top:346px;font-size:5.4px;color:var(--muted);line-height:1.5}
.dental{position:absolute;left:258px;top:0;right:0}
.dental-head{background:var(--navy);color:#fff;font-weight:700;font-size:8px;padding:6px;height:30px;display:flex;align-items:center}
.dental .vd-table th{background:#3c3a6a;color:#fff;font-weight:600}
.dental .vd-table .lbl{background:#8f8fae;color:#fff;font-weight:600;width:28%}
.dental .vd-table .val{background:var(--dental-row)}
.dental .vd-table tr:nth-child(even) .val{background:#c9c9e4}
.ortho{margin-top:6px}
.dental-badge{position:absolute;left:176px;top:196px;width:50px;height:50px;border-radius:50%;background:var(--navy);color:#fff;font-size:6px;font-weight:700;display:flex;flex-direction:column;align-items:center;justify-content:center;text-align:center;line-height:1.3}
.dental-note{position:absolute;left:60px;top:206px;font-size:5.4px;color:var(--muted);line-height:1.5}
</style>
</head>
<body>

<section class="page page--medical">
  <header class="page-head">
    <div class="brand">Brisk Lending</div>
    <h1 class="page-title">Medical plans</h1>
  </header>

  <div class="plan-grid">
    <div class="corner"></div>
    <div class="plan-head h1">Crestline Bronze HSA<small>Lowest premium</small></div>
    <div class="plan-head h2">Crestline Silver HSA<small>Balanced option</small></div>
    <div class="plan-head h3">Crestline Gold PPO<small>Broad network</small></div>
    <div class="plan-head h4">Crestline Select PPO<small>Lower copays</small></div>
    <div class="plan-head h5">Crestline Platinum PPO<small>Richest coverage</small></div>

    <div class="row-label sub"></div>
    <div class="c1 sub">In-network</div><div class="c1 sub">Out-of-network</div>
    <div class="c2 sub">In-network</div><div class="c2 sub">Out-of-network</div>
    <div class="c3 sub">In-network</div><div class="c3 sub">Out-of-network</div>
    <div class="c4 sub">In-network</div><div class="c4 sub">Out-of-network</div>
    <div class="c5 sub">In-network</div><div class="c5 sub">Out-of-network</div>

    <div class="row-label">Primary Care Visit</div>
    <div class="c1">20% after ded.</div><div class="c1">40% after ded.</div>
    <div class="c2">20% after ded.</div><div class="c2">40% after ded.</div>
    <div class="c3">$25 copay</div><div class="c3">30% after ded.</div>
    <div class="c4">$20 copay</div><div class="c4">30% after ded.</div>
    <div class="c5">$10 copay</div><div class="c5">20% after ded.</div>

    <div class="row-label">Specialist Visit</div>
    <div class="c1">20% after ded.</div><div class="c1">40% after ded.</div>
    <div class="c2">20% after ded.</div><div class="c2">40% after ded.</div>
    <div class="c3">$50 copay</div><div class="c3">30% after ded.</div>
    <div class="c4">$40 copay</div><div class="c4">30% after ded.</div>
    <div class="c5">$20 copay</div><div class="c5">20% after ded.</div>

    <div class="row-label">Preventive Care</div>
    <div class="c1">No charge</div><div class="c1">40% after ded.</div>
    <div class="c2">No charge</div><div class="c2">40% after ded.</div>
    <div class="c3">No charge</div><div class="c3">30% after ded.</div>
    <div class="c4">No charge</div><div class="c4">30% after ded.</div>
    <div class="c5">No charge</div><div class="c5">20% after ded.</div>

    <div class="row-label">Deductible (Individual / Family)</div>
    <div class="c1">$6,000 / $12,000</div><div class="c1">$12,000 / $24,000</div>
    <div class="c2">$3,500 / $7,000</div><div class="c2">$7,000 / $14,000</div>
    <div class="c3">$2,000 / $4,000</div><div class="c3">$4,000 / $8,000</div>
    <div class="c4">$1,000 / $2,000</div><div class="c4">$2,000 / $4,000</div>
    <div class="c5">$0 / $0</div><div class="c5">$500 / $1,000</div>

    <div class="row-label">Out-of-Pocket Max (Ind. / Fam.)</div>
    <div class="c1">$7,000 / $14,000</div><div class="c1">$14,000 / $28,000</div>
    <div class="c2">$6,500 / $13,000</div><div class="c2">$13,000 / $26,000</div>
    <div class="c3">$5,000 / $10,000</div><div class="c3">$10,000 / $20,000</div>
    <div class="c4">$4,000 / $8,000</div><div class="c4">$8,000 / $16,000</div>
    <div class="c5">$2,500 / $5,000</div><div class="c5">$5,000 / $10,000</div>

    <div class="row-label">Coinsurance</div>
    <div class="c1">20%</div><div class="c1">40%</div>
    <div class="c2">20%</div><div class="c2">40%</div>
    <div class="c3">10%</div><div class="c3">30%</div>
    <div class="c4">10%</div><div class="c4">30%</div>
    <div class="c5">0%</div><div class="c5">20%</div>

    <div class="row-label">Emergency Room</div>
    <div class="c1">20% after ded.</div><div class="c1">20% after ded.</div>
    <div class="c2">20% after ded.</div><div class="c2">20% after ded.</div>
    <div class="c3">$300 copay</div><div class="c3">$300 copay</div>
    <div class="c4">$250 copay</div><div class="c4">$250 copay</div>
    <div class="c5">$150 copay</div><div class="c5">$150 copay</div>

    <div class="row-label">Urgent Care</div>
    <div class="c1">20% after ded.</div><div class="c1">40% after ded.</div>
    <div class="c2">20% after ded.</div><div class="c2">40% after ded.</div>
    <div class="c3">$50 copay</div><div class="c3">30% after ded.</div>
    <div class="c4">$40 copay</div><div class="c4">30% after ded.</div>
    <div class="c5">$25 copay</div><div class="c5">20% after ded.</div>

    <div class="row-label">Hospital Stay</div>
    <div class="c1">20% after ded.</div><div class="c1">40% after ded.</div>
    <div class="c2">20% after ded.</div><div class="c2">40% after ded.</div>
    <div class="c3">10% after ded.</div><div class="c3">30% after ded.</div>
    <div class="c4">10% after ded.</div><div class="c4">30% after ded.</div>
    <div class="c5">$250 per stay</div><div class="c5">20% after ded.</div>

    <div class="row-label">Prescription Drugs</div>
    <div class="c1">$10 / $40 / $70</div><div class="c1">Not covered</div>
    <div class="c2">$10 / $35 / $60</div><div class="c2">Not covered</div>
    <div class="c3">$10 / $30 / $50</div><div class="c3">Not covered</div>
    <div class="c4">$5 / $25 / $45</div><div class="c4">Not covered</div>
    <div class="c5">$5 / $20 / $40</div><div class="c5">Not covered</div>
  </div>

  <div class="cost-band">
    <div class="cost-label">Per Paycheck Cost<br>Employee<br>Employee + Spouse<br>Family</div>
    <div class="cost-value"><br>$22.00<br>$64.50<br>$98.20</div>
    <div class="cost-value"><br>$36.00<br>$82.40<br>$121.70</div>
    <div class="cost-value"><br>$48.50<br>$104.00<br>$152.30</div>
    <div class="cost-value"><br>$61.00<br>$128.60<br>$184.90</div>
    <div class="cost-value"><br>$79.00<br>$156.20<br>$221.40</div>
  </div>

  <div class="badges">
    <div class="badge-note">Monthly HSA Contribution<br>Company funded for<br>eligible plans only</div>
    <div class="badge b1"><span>$750</span>HSA funded</div>
    <div class="badge b2"><span>$500</span>HSA funded</div>
    <div class="badge b3"><span>PPO</span>Any doctor</div>
    <div class="badge b4"><span>PPO</span>Low copays</div>
    <div class="badge b5"><span>$0</span>Deductible</div>
  </div>

  <p class="footnote">This summary is a guide only and does not replace official plan documents. Costs shown are per paycheck with 24 pay periods per year. Please review the full plan details before making your elections during open enrollment.</p>
</section>

<section class="page page--dental">
  <header class="page-head">
    <div class="brand">Brisk Lending</div>
    <h1 class="page-title">Vision | Dental plans</h1>
  </header>

  <div class="vd-layout">
    <div class="vision">
      <div class="vision-head">Vision</div>
      <table class="vd-table">
        <tr><td class="lbl">Eye Exam</td><td class="val">$10 copay once every 12 months</td></tr>
        <tr><td class="lbl">Frames</td><td class="val">$150 allowance every 24 months<br>20% off amount over allowance</td></tr>
        <tr><td class="lbl">Lenses</td><td class="val">Single vision $25 copay<br>Bifocal $25 copay<br>Trifocal $25 copay</td></tr>
        <tr><td class="lbl">Contact Lenses</td><td class="val">$150 allowance instead of glasses<br>Fitting exam up to $60</td></tr>
        <tr><td class="lbl">Lens Options</td><td class="val">Anti-glare $40 copay<br>Scratch coating $15 copay<br>Tint $15 copay</td></tr>
        <tr><td class="lbl">Out-of-Network</td><td class="val">Exam up to $45<br>Frames up to $70<br>Lenses up to $50</td></tr>
        <tr><td class="lbl">Laser Vision</td><td class="val">Up to 15% off standard price</td></tr>
        <tr><td class="lbl">Extra Savings</td><td class="val">20% off a second pair of glasses</td></tr>
      </table>
      <p class="vision-note">Monthly Cost<br>Employee $6.20<br>Family $17.40</p>
      <div class="vision-badge"><span>$6</span>per month</div>
    </div>

    <div class="dental">
      <div class="dental-head">Dental</div>
      <table class="vd-table">
        <tr><th></th><th colspan="2">Crestline Base</th><th colspan="2">Crestline Enhanced</th></tr>
        <tr><th></th><th>In-network</th><th>Out-network</th><th>In-network</th><th>Out-network</th></tr>
        <tr><td class="lbl">Deductible</td><td class="val">$50 / $150</td><td class="val">$50 / $150</td><td class="val">$25 / $75</td><td class="val">$25 / $75</td></tr>
        <tr><td class="lbl">Annual Max</td><td class="val">$1,000</td><td class="val">$1,000</td><td class="val">$2,000</td><td class="val">$2,000</td></tr>
        <tr><td class="lbl">Preventive</td><td class="val">100%</td><td class="val">80%</td><td class="val">100%</td><td class="val">100%</td></tr>
        <tr><td class="lbl">Basic</td><td class="val">80%</td><td class="val">60%</td><td class="val">90%</td><td class="val">80%</td></tr>
        <tr><td class="lbl">Major</td><td class="val">50%</td><td class="val">40%</td><td class="val">60%</td><td class="val">50%</td></tr>
      </table>
      <table class="vd-table ortho">
        <tr><td class="lbl">Orthodontia</td><td class="val">Not covered</td><td class="val">Not covered</td><td class="val">50% to $1,500</td><td class="val">50% to $1,500</td></tr>
      </table>
      <p class="dental-note">Monthly Cost<br>Employee $4.80</p>
      <div class="dental-badge"><span>$5</span>per month</div>
    </div>
  </div>

  <p class="footnote">This summary is a guide only and does not replace official plan documents. Network providers offer the lowest cost. Out-of-network claims are paid up to the allowed amount and you may owe any balance over that.</p>
</section>

</body>
</html>
```